Premium Classic Tea Box Packaging Design

We are going to launch a new product of premium classic tea using Tongkat Ali ingredient. We are looking for the tea box packaging design for our product that named Qiu Ran 秋然. Both english and chinese name should be included in the packaging design. Product origin from Malaysia.

Other things that should be included in the design are
- website url "www.qiuran.my"
- Premium Tea
- Slogan "Live Live to the Fullest
- 100% All Natural Ingredients
- 养生保健,首选咖啡

The product content is 20 tea bags. The size of the package is rectangular, Size: Box - 180 x 125 x 40 mm (Pizza Box Style of opening). Consumers would open the packaging box and see the tea bags lies inside similar to this . http://vbrlk.io/Rm7Tq2

We are looking for design that gives us the feeling of
- classy feeling
- strong
- confidence
- a combination of chinese and western design style (optional)
- gentleman
- expensive / high end

This is a premium product and design should symbolise health, hope, wellness and prosperity

We would like to see designs that use the shining color
- shining black
- gold
- green
However if you deem that other colors can be more suitable, we are open to new ideas.

I am looking for creative ideas that are able to capture people attention with its elegance.

Example of designs that we like :
http://vbrlk.io/Hp3Wz8
http://vbrlk.io/Kx9Fa4
http://vbrlk.io/Nd2Ys6
http://vbrlk.io/Gq5Lm1
http://vbrlk.io/Wc8Pe3 / http://vbrlk.io/Jt4Hv7
http://vbrlk.io/Sa6Ku9
http://vbrlk.io/Ey1Rb5
http://vbrlk.io/Mf7Xo2

Close/Similar company to reference : KRP / Premium Haldwicks

Reason: Hi all, thank you for your submission. We will be replying to proposal and discuss improvements that could be make, if possible, please try to change design to using dark -ish shining green as background. For those who intending to submit your proposal, please do so. Thank you for all the proposal.

Target Market(s)

Our target market men from the China market.

Industry/Entity Type

Health And Wellness

Font styles to use
Decorative
Script

Requirements
Must have
• Both english and chinese name should be included in the packaging design. Product origin from Malaysia.
• Other things that should be included in the design are
• - website url "www.qiuran.my"
• - Premium Tea
• - Slogan "Live Live to the Fullest
• - 100% All Natural Ingredients
• - 养生保健,首选咖啡

```html
<!DOCTYPE html>
<html lang="en">
<head>
<meta charset="utf-8">
<title>Qiu Ran Premium Tea – Box Dieline</title>
<link rel="stylesheet" href="https://fonts.googleapis.com/css2?family=Marcellus&family=Cormorant+Garamond:ital,wght@1,500&family=Noto+Serif+SC:wght@500&family=Cinzel:wght@500&display=swap">
<style>
  :root {
    --canvas: #ffffff;
    --green-light: #3d6b24;
    --green-mid: #2c5019;
    --green-dark: #1f3812;
    --strip: #274716;
    --gold: #e9b47c;
    --gold-soft: #d8a56e;
    --fold: #c9cfc3;
    --vine: #183010;
  }
  html, body {
    margin: 0;
    padding: 0;
    width: 1082px;
    height: 1200px;
    overflow: hidden;
    background: var(--canvas);
  }
  .dieline {
    position: absolute;
    left: 41px;
    top: 258px;
    width: 1000px;
    height: 683px;
  }
  .board { fill: var(--green-mid); }
  .panel-front { fill: url(#panelGlow); }
  .panel-lid { fill: url(#panelGlowWide); }
  .side-strip { fill: var(--strip); }
  .fold { fill: none; stroke: var(--fold); stroke-width: 0.6; stroke-dasharray: 2.4 1.8; }
  .vine { fill: var(--vine); opacity: 0.45; }
  .kicker { font-family: 'Cinzel', serif; fill: var(--gold-soft); letter-spacing: 0.8px; }
  .brand { font-family: 'Marcellus', serif; fill: var(--gold); letter-spacing: 0.6px; }
  .brand-cn { font-family: 'Noto Serif SC', serif; fill: var(--gold); }
  .slogan { font-family: 'Cormorant Garamond', serif; font-style: italic; font-weight: 500; fill: var(--gold); letter-spacing: 0.6px; }
  .fine { font-family: 'Cinzel', serif; fill: var(--gold-soft); letter-spacing: 0.4px; }
</style>
</head>
<body>
<svg class="dieline" viewBox="0 0 600 410" xmlns="http://www.w3.org/2000/svg">
  <defs>
    <radialGradient id="panelGlow" cx="50%" cy="42%" r="65%">
      <stop offset="0" stop-color="var(--green-light)"/>
      <stop offset="1" stop-color="var(--green-dark)"/>
    </radialGradient>
    <radialGradient id="panelGlowWide" cx="50%" cy="50%" r="70%">
      <stop offset="0" stop-color="var(--green-light)"/>
      <stop offset="1" stop-color="var(--green-dark)"/>
    </radialGradient>
  </defs>

  <!-- board outline -->
  <rect class="board" x="5" y="62" width="230" height="335" rx="12"/>
  <rect class="board" x="222" y="4" width="373" height="398" rx="10"/>

  <!-- panels -->
  <rect class="panel-lid" x="55" y="67" width="167" height="305"/>
  <rect class="side-strip" x="222" y="4" width="60" height="398" rx="8"/>
  <rect class="panel-front" x="282" y="67" width="178" height="270"/>
  <rect class="side-strip" x="460" y="67" width="60" height="270"/>

  <!-- fold lines -->
  <line class="fold" x1="55" y1="62" x2="55" y2="397"/>
  <line class="fold" x1="222" y1="62" x2="222" y2="397"/>
  <line class="fold" x1="282" y1="4" x2="282" y2="402"/>
  <line class="fold" x1="460" y1="4" x2="460" y2="402"/>
  <line class="fold" x1="520" y1="4" x2="520" y2="402"/>
  <line class="fold" x1="222" y1="67" x2="595" y2="67"/>
  <line class="fold" x1="222" y1="337" x2="595" y2="337"/>
  <line class="fold" x1="55" y1="72" x2="222" y2="72"/>
  <line class="fold" x1="55" y1="367" x2="222" y2="367"/>
  <rect class="fold" x="290" y="12" width="162" height="48"/>
  <rect class="fold" x="290" y="344" width="162" height="50"/>
  <rect class="fold" x="62" y="77" width="153" height="283"/>

  <!-- leaf vine areas -->
  <rect class="vine" x="285" y="232" width="40" height="95" rx="6" role="img" aria-label="Tea leaf vine illustration"/>
  <rect class="vine" x="420" y="182" width="40" height="110" rx="6" role="img" aria-label="Tea leaf vine illustration"/>
  <rect class="vine" x="60" y="77" width="80" height="35" rx="6" role="img" aria-label="Tea leaf vine illustration"/>
  <rect class="vine" x="50" y="287" width="110" height="35" rx="6" role="img" aria-label="Tea leaf vine illustration"/>

  <!-- top flap -->
  <g class="top-flap" text-anchor="middle">
    <text class="kicker" x="371" y="25" font-size="5">PREMIUM TEA</text>
    <text class="brand" x="371" y="42" font-size="12">QIU RAN</text>
    <text class="brand-cn" x="371" y="54" font-size="7">秋然</text>
  </g>

  <!-- front panel -->
  <g class="front" text-anchor="middle">
    <text class="kicker" x="371" y="135" font-size="6.5">PREMIUM TEA</text>
    <text class="brand" x="371" y="160" font-size="19">QIU RAN</text>
    <text class="brand-cn" x="371" y="177" font-size="10">秋然</text>
    <text class="slogan" x="371" y="223" font-size="8">Live Live to the Fullest</text>
    <text class="fine" x="371" y="302" font-size="4.6">Product of Malaysia</text>
    <text class="fine" x="371" y="310" font-size="4.6">www.qiuran.my</text>
  </g>

  <!-- bottom flap, printed upside down -->
  <g class="bottom-flap" text-anchor="middle" transform="rotate(180 371 369)">
    <text class="fine" x="371" y="367" font-size="5">100% All Natural Ingredients</text>
    <text class="brand-cn" x="371" y="377" font-size="5">养生保健，首选咖啡</text>
  </g>

  <!-- left side strip -->
  <g class="side-left" text-anchor="middle" transform="rotate(90 252 205)">
    <text class="kicker" x="252" y="190" font-size="5">PREMIUM TEA</text>
    <text class="brand" x="252" y="203" font-size="12">QIU RAN</text>
    <text class="brand-cn" x="252" y="215" font-size="7">秋然</text>
  </g>

  <!-- right side strip -->
  <g class="side-right" text-anchor="middle" transform="rotate(90 490 205)">
    <text class="kicker" x="490" y="190" font-size="5">PREMIUM TEA</text>
    <text class="brand" x="490" y="203" font-size="12">QIU RAN</text>
    <text class="brand-cn" x="490" y="215" font-size="7">秋然</text>
  </g>

  <!-- lid panel -->
  <g class="lid" text-anchor="middle" transform="rotate(90 138 205)">
    <text class="kicker" x="138" y="155" font-size="6">PREMIUM TEA</text>
    <text class="brand" x="138" y="174" font-size="16">QIU RAN</text>
    <text class="brand-cn" x="138" y="187" font-size="9">秋然</text>
    <text class="slogan" x="138" y="209" font-size="7">Live Live to the Fullest</text>
    <text class="fine" x="138" y="240" font-size="4.4">Product of Malaysia</text>
    <text class="fine" x="138" y="247" font-size="4.4">www.qiuran.my</text>
  </g>
</svg>
</body>
</html>
```